The Marlow Wellness Studio (marlowstudio.example)

One page website (already purchased the theme) introducing the online clinic, with video, sections on the page our process, the technology, blog, the practitioner, contact, testimonials, find out more (see copy below) I am in the closing stages of having some collateral prepared I will load up the files that are in place so far so you get the feel for the brand and the current progress on the a brochure. The theme I have currently is loaded with demo data . this needs to be deleted and replaced. See here marlowstudio.example.

Target Market(s)

Female 30-50

Coding

Coded - Design and coding required

Number of Pages Required

1 page

Font styles to use
Serif
Sans Serif

Colors
33a6d7
3277b5

Requirements
Must have
• Consistent feel with existing A4 brochure, Trifold Brochure and business card,

Intro image & Outcome statement - Recharge Your Energy
Video & Free Access Offer
Why Energy
Our Process
About Vireq Technology
Getting Started
About Tobin
Our Services
Testimonials
Contact
Blog

Nice to have
• Suggestions for images.

```html
<!DOCTYPE html>
<html lang="en">
<head>
<meta charset="utf-8">
<title>The Marlow Wellness Studio</title>
<link href="https://fonts.googleapis.com/css2?family=Playfair+Display:wght@400&family=Lato:ital,wght@0,300;0,400;0,700;1,400&family=Roboto:wght@500;700&display=swap" rel="stylesheet">
<style>
:root{
  --sky:#33a6d7;
  --blue:#3277b5;
  --navy:#2c66a8;
  --ink:#2b2b2b;
  --text:#555;
  --white:#fff;
  --footer:#2e2e2e;
  --serif:'Playfair Display',serif;
  --sans:'Lato',sans-serif;
  --ui:'Roboto',sans-serif;
}
*{box-sizing:border-box;margin:0;padding:0}
html,body{width:1200px;height:3983px;overflow:hidden;background:var(--white)}
body{position:relative;font-family:var(--sans);color:var(--text)}
.abs{position:absolute}
.section{position:absolute;left:0;width:1200px}

/* header */
.header{top:0;height:74px}
.brand{left:144px;top:14px;display:flex;align-items:center;gap:10px;font-family:var(--sans);font-weight:700;font-size:21px;color:var(--sky)}
.brand-dot{width:40px;height:40px;border-radius:50%;background:#cfd6da}
.phone{right:144px;top:14px;display:flex;align-items:center;gap:10px;font-family:var(--ui);font-weight:700;font-size:24px;color:var(--ink)}
.nav{top:74px;height:44px;background:var(--blue)}
.nav ul{list-style:none;display:flex;position:absolute;left:144px;top:0;height:44px}
.nav li{font-family:var(--ui);font-weight:700;font-size:14px;color:var(--white);padding:0 15px;line-height:44px}
.nav li.active{background:var(--sky);padding:0 21px}

/* hero */
.hero{top:118px;height:664px;background:linear-gradient(180deg,#e9c9a4 0%,#d49a5c 35%,#b7743f 60%,#6f4c35 100%)}
.hero h1{position:absolute;top:106px;width:100%;text-align:center;font-family:var(--serif);font-weight:400;font-size:72px;color:var(--white)}
.hero p{position:absolute;top:238px;width:100%;text-align:center;font-size:28px;line-height:39px;color:var(--white)}
.btn{display:inline-block;background:var(--blue);color:var(--white);font-family:var(--ui);font-weight:700;font-size:14px;text-align:center}
.btn-sky{background:var(--sky)}
.hero .btn{position:absolute;left:498px;top:358px;width:204px;height:50px;line-height:50px}
.play{position:absolute;left:554px;top:447px}

/* about blocks */
.eyebrow{font-family:var(--ui);font-weight:500;font-size:16px;color:var(--sky)}
.title{font-family:var(--serif);font-weight:400;font-size:52px;color:var(--ink)}
.copy{font-family:var(--sans);font-weight:300;font-size:16px;line-height:26.3px;color:#555}
.btn-block{height:43px;line-height:43px}
.photo{border-radius:50%}

/* process */
.process{top:1302px;height:521px;background:var(--sky)}
.center-eyebrow{position:absolute;width:100%;text-align:center;font-family:var(--ui);font-weight:500;font-size:16px;color:var(--white)}
.center-title{position:absolute;width:100%;text-align:center;font-family:var(--serif);font-weight:400;font-size:52px;color:var(--white)}
.tile{position:absolute;overflow:hidden;color:var(--white);text-align:center}
.tile-label{position:absolute;width:100%;font-family:var(--sans);font-size:26px}
.tile-text{position:absolute;width:100%;padding:0 22px;font-size:14px;line-height:22px}
.chev{position:absolute;left:50%;margin-left:-9px}

/* testimonials */
.clients{top:2437px;height:604px;background:var(--blue)}
.quote{position:absolute;top:258px;width:285px;height:250px;background:var(--white);border-radius:4px;text-align:center;padding:76px 20px 0}
.avatar{position:absolute;top:-64px;left:50%;margin-left:-46px;width:92px;height:92px;border-radius:50%;border:3px solid var(--white)}
.quote h4{font-family:var(--ui);font-weight:700;font-size:13px;color:var(--ink)}
.qmark{font-family:var(--serif);font-style:italic;font-size:30px;color:var(--sky);line-height:30px;margin-top:4px}
.quote p{font-style:italic;font-size:13px;line-height:20.5px;color:#666}

/* blog */
.blog{top:3041px;height:549px}
.blog h2{position:absolute;top:66px;width:100%;text-align:center;font-family:var(--serif);font-weight:400;font-size:52px;color:var(--ink)}
.post-date{position:absolute;width:100%;font-size:18px;font-weight:700}
.post-title{position:absolute;width:100%;font-size:20px;font-weight:700}

/* footer */
.footer{top:3590px;height:393px;background:var(--footer);color:#ddd}
.footer .brand{left:170px;top:96px;font-size:32px;gap:14px}
.footer .brand-dot{width:54px;height:54px;background:#e8e8e8}
.f-info{position:absolute;left:170px;top:170px;font-size:16px;line-height:26px;color:#eee}
.f-head{position:absolute;top:70px;font-family:var(--ui);font-weight:700;font-size:20px;color:var(--sky)}
.f-links{position:absolute;left:571px;top:115px;list-style:none;font-size:15px;line-height:30px;color:#eee}
.social{position:absolute;top:118px;left:843px;display:flex;gap:9px}
.social span{width:40px;height:40px;border-radius:50%;background:var(--white)}
.copyright{position:absolute;top:343px;width:100%;text-align:center;font-size:14px;color:#eee}
</style>
</head>
<body>

<header class="section header">
  <div class="abs brand"><span class="brand-dot"></span>The Marlow Wellness Studio</div>
  <div class="abs phone">
    <svg width="40" height="40" viewBox="0 0 40 40" aria-hidden="true"><circle cx="20" cy="20" r="18" fill="none" stroke="#33a6d7" stroke-width="3"/><path d="M14 11c1-1 3-1 4 1l2 3c.6 1 .3 2-.5 2.6l-1.5 1c1 2.5 3 4.5 5.5 5.5l1-1.5c.6-.8 1.6-1.1 2.6-.5l3 2c2 1 2 3 1 4-2 2-5 2.5-8 1-4-2-8-6-10-10-1.5-3-1-6 1-8z" fill="#33a6d7"/></svg>
    800-555-0142
  </div>
</header>

<nav class="section nav">
  <ul>
    <li class="active">HOME</li><li>OUR PROCESS</li><li>WHO ARE WE</li><li>TESTIMONIALS</li><li>ABOUT VIREQ TECHNOLOGY</li><li>BLOG</li><li>CONTACT</li>
    <li><svg width="14" height="14" viewBox="0 0 14 14" aria-hidden="true"><circle cx="6" cy="6" r="4.5" fill="none" stroke="#fff" stroke-width="2"/><path d="M9.5 9.5L13 13" stroke="#fff" stroke-width="2"/></svg></li>
  </ul>
</nav>

<section class="section hero" role="img" aria-label="Woman leaping joyfully on a beach at sunset">
  <h1>The Marlow Wellness Studio</h1>
  <p>Lorem ipsum dolor sit amet consectetur adipiscing elit<br>sed do eiusmod tempor incididunt</p>
  <span class="btn btn-sky">FREE ACCESS OFFER</span>
  <svg class="play" width="92" height="92" viewBox="0 0 92 92" aria-label="Play video"><circle cx="46" cy="46" r="42" fill="none" stroke="#fff" stroke-width="5"/><path d="M36 27L66 46L36 65Z" fill="#fff"/></svg>
</section>

<section class="section" style="top:782px;height:520px">
  <div class="abs eyebrow" style="left:170px;top:60px">ABOUT</div>
  <h2 class="abs title" style="left:170px;top:88px">Who Are We</h2>
  <p class="abs copy" style="left:170px;top:168px;width:510px">It took Tobin almost 3 decades of trial and error, and false hope, for him to arrive at the same conclusion that leading experts in the field of bioenergetics had been saying since the beginning: energy drives biochemistry, not the other way round.”in essence, Vireq gives you night goggles on what is going on for you, moreover what you can do about it. This is truly the future of medicine” Tobin R Halvorsen.He has adopted the Vireq Health approach to supporting his</p>
  <span class="abs btn btn-block" style="left:170px;top:387px;width:128px">READ MORE</span>
  <div class="abs photo" style="left:733px;top:120px;width:296px;height:296px;background:radial-gradient(circle at 40% 40%,#e8ecef,#9aa9b4 70%,#6c7d88)" role="img" aria-label="Practitioner talking with a client"></div>
</section>

<section class="section process">
  <div class="center-eyebrow" style="top:82px">HOW WE HELP</div>
  <h2 class="center-title" style="top:110px">Our Process</h2>
  <div class="tile" style="left:144px;top:222px;width:290px;height:214px;background:linear-gradient(180deg,#fafafa,#bdbdbd 60%,#6e6e6e)" role="img" aria-label="Body scan figure surrounded by energy rings">
    <div class="tile-label" style="top:132px">Detect</div>
    <svg class="chev" style="top:176px" width="18" height="12" viewBox="0 0 18 12"><path d="M2 2l7 7 7-7" fill="none" stroke="#fff" stroke-width="2"/></svg>
  </div>
  <div class="tile" style="left:453px;top:222px;width:292px;height:214px;background:linear-gradient(180deg,#5a4a36,#2a241d)" role="img" aria-label="Practitioner guiding a client through the software">
    <div class="tile-label" style="top:30px">Direct</div>
    <div class="tile-text" style="top:74px">Ffollow the steps in the software to get the fastest possible results See beyond your client's symptoms,</div>
    <svg class="chev" style="top:166px" width="18" height="12" viewBox="0 0 18 12"><path d="M2 10l7-7 7 7" fill="none" stroke="#fff" stroke-width="2"/></svg>
  </div>
  <div class="tile" style="left:764px;top:222px;width:290px;height:214px;background:linear-gradient(180deg,#f2f2f2,#b9b9b9 60%,#777)" role="img" aria-label="Row of dropper bottles">
    <div class="tile-label" style="top:132px">Correct</div>
    <svg class="chev" style="top:176px" width="18" height="12" viewBox="0 0 18 12"><path d="M2 2l7 7 7-7" fill="none" stroke="#fff" stroke-width="2"/></svg>
  </div>
</section>

<section class="section" style="top:1823px;height:614px">
  <div class="abs eyebrow" style="left:144px;top:117px">ABOUT</div>
  <h2 class="abs title" style="left:144px;top:142px">Vireq Technology</h2>
  <p class="abs copy" style="left:144px;top:226px;width:450px">Sed ut perspiciatis unde omnis iste natus error sit voluptatem accusantium doloremque laudantium, totam rem aperiam, eaque ipsa quae ab illo inventore veritatis et quasi architecto beatae vitae dicta sunt explicabemo enim ipsam voluptatem quia voluptas sit aspernatur aut odit aut fugit, sed quia consequuntur magni dolores eos qui ratione voluptatem sequi nesciunt. Neque porro quisquam est, qui dolorem ipsum quia dolor sit amet, consectetu</p>
  <span class="abs btn btn-block" style="left:144px;top:471px;width:128px">READ MORE</span>
  <svg class="abs" style="left:625px;top:84px" width="450" height="440" viewBox="0 0 450 440" aria-hidden="true"><circle cx="225" cy="220" r="210" fill="none" stroke="#33a6d7" stroke-width="9" stroke-dasharray="760 560" stroke-dashoffset="-180"/></svg>
  <div class="abs photo" style="left:629px;top:97px;width:412px;height:412px;background:linear-gradient(120deg,#e9e6e1 0%,#c9c3b9 45%,#e3b92c 75%,#c99a1c)" role="img" aria-label="Client on a video consultation with a doctor on a laptop"></div>
</section>

<section class="section clients">
  <div class="center-eyebrow" style="top:92px">CLIENTS</div>
  <h2 class="center-title" style="top:120px">What Clients Say</h2>
  <div class="quote" style="left:145px">
    <div class="avatar" style="background:linear-gradient(180deg,#e7d4b0,#f2ede6)" role="img" aria-label="Portrait of Dr Helen Carrow"></div>
    <h4>DR HELEN CARROW</h4><div class="qmark">“</div>
    <p>“Vireq Health truly offers insights into the body, both mind and physical well-being, that the medical community cannot comprehend often, nor understand. It is truly a remarkable system”</p>
  </div>
  <div class="quote" style="left:458px">
    <div class="avatar" style="background:linear-gradient(180deg,#5a4636,#cfd2d6)" role="img" aria-label="Portrait of Dr. Owen Pritchard"></div>
    <h4>DR. OWEN PRITCHARD. MD</h4><div class="qmark">“</div>
    <p>“provides the signal for the body to heal itself. What's hard to understand is it really doesn't do anything except provide the signal. The body does everything else”</p>
  </div>
  <div class="quote" style="left:770px">
    <div class="avatar" style="background:linear-gradient(180deg,#e8e4dc,#cbbfb0)" role="img" aria-label="Portrait of Maria Dunmore"></div>
    <h4>MARIA DUNMORE</h4><div class="qmark">“</div>
    <p>“Thanks to Vireq, my energy has skyrocketed and I am accomplishing more than I have in years”</p>
  </div>
</section>

<section class="section blog">
  <h2>Blog Posts</h2>
  <div class="tile" style="left:145px;top:170px;width:286px;height:212px;background:linear-gradient(180deg,#8fa6b7,#c8d4dc 55%,#93a9b8)" role="img" aria-label="Stacked pebbles on raked sand">
    <div class="post-date" style="top:112px">FEB 2020</div>
    <div class="post-title" style="top:144px">Lorem ipsum dolsmet</div>
    <svg class="chev" style="top:182px" width="18" height="12" viewBox="0 0 18 12"><path d="M2 2l7 7 7-7" fill="none" stroke="#fff" stroke-width="2"/></svg>
  </div>
  <div class="tile" style="left:458px;top:170px;width:285px;height:212px;background:linear-gradient(180deg,#4d4d4d,#6a6a6a)" role="img" aria-label="Practitioner working at a desk">
    <div class="post-date" style="top:30px">FEB 2020</div>
    <div class="post-title" style="top:62px">Lorem ipsum dolsmet</div>
    <div class="tile-text" style="top:104px;font-size:13px;line-height:19px">Lorem ipsum dolor sit aconsectetur adipiscing elid do eiusmod tempor incididunt ut labore et dolor</div>
    <svg class="chev" style="top:172px" width="18" height="12" viewBox="0 0 18 12"><path d="M2 10l7-7 7 7" fill="none" stroke="#fff" stroke-width="2"/></svg>
  </div>
  <div class="tile" style="left:770px;top:170px;width:285px;height:212px;background:linear-gradient(180deg,#2a4b3c,#3e6553 50%,#1f3a30)" role="img" aria-label="Woman meditating in a forest by water">
    <div class="post-date" style="top:112px">FEB 2020</div>
    <div class="post-title" style="top:144px">Lorem ipsum dolsmet</div>
    <svg class="chev" style="top:182px" width="18" height="12" viewBox="0 0 18 12"><path d="M2 2l7 7 7-7" fill="none" stroke="#fff" stroke-width="2"/></svg>
  </div>
  <span class="abs btn btn-block" style="left:536px;top:426px;width:128px">VIEW MORE</span>
</section>

<footer class="section footer">
  <div class="abs brand"><span class="brand-dot"></span>marlowstudio.example</div>
  <div class="f-info">info@marlowstudio.example<br>612 9000 4415<br>Level 8, 42 Harbour Lane, Sydney, Australia</div>
  <div class="f-head" style="left:571px">QUICK LINKS</div>
  <ul class="f-links"><li>Our Process</li><li>Who are We</li><li>Testimonials</li><li>About Vireq Technology</li><li>Blog</li><li>Contact</li></ul>
  <div class="f-head" style="left:843px">STAY CONNECTED</div>
  <div class="social" aria-label="Social links"><span></span><span></span><span></span></div>
  <div class="copyright">© 2020 The Marlow Wellness Studio. All rights reserved &nbsp;|&nbsp; Privacy Policy &nbsp;|&nbsp; Terms and Use</div>
</footer>

</body>
</html>
```